Cleaning services Business Card Design

I need a business card design for my Cleaning business. I would like perhaps emphasis on the company name, Muddle to Marvel. Maybe the Muddle would to dirty and the marvel would have sprinkles.

Industry/Entity Type

Business

Contact Information for Business Card

Muddle to Marvel Cleaning Services, Teodoro Perlas, Industrial, Commercial, & Residential 418-635-0247

```html
<!DOCTYPE html>
<html lang="en">
<head>
<meta charset="utf-8">
<title>Muddle to Marvel Cleaning Services – Business Card</title>
<link rel="stylesheet" href="https://fonts.googleapis.com/css2?family=Open+Sans:ital,wght@0,400;0,600;0,800;1,400&display=swap">
<style>
  :root {
    --page-bg: #4a4a4a;
    --card-white: #ffffff;
    --card-black: #050505;
    --ink-dark: #1a1a1a;
    --ink-grey: #555555;
    --ink-light: #e4e4e4;
    --tagline-grey: #9a9a9a;
    --brand-blue: #1e90e8;
    --rule: #444444;
  }
  * { margin: 0; padding: 0; box-sizing: border-box; }
  html, body {
    width: 1105px; height: 1200px; overflow: hidden;
    background: var(--page-bg);
    font-family: "Open Sans", Arial, sans-serif;
  }
  .card {
    position: absolute;
    left: 192px;
    width: 720px;
    height: 412px;
  }
  .card--front { top: 146px; background: var(--card-white); }
  .card--back { top: 602px; background: var(--card-black); overflow: hidden; }

  .brand { position: absolute; text-align: center; }
  .brand__name {
    font-weight: 800;
    font-size: 41px;
    line-height: 1;
    letter-spacing: 0.5px;
    text-transform: uppercase;
    white-space: nowrap;
  }
  .brand__tagline {
    font-weight: 400;
    font-size: 17px;
    letter-spacing: 10.5px;
    text-transform: uppercase;
    margin-top: 10px;
    margin-right: -10.5px;
    white-space: nowrap;
  }
  .card--front .brand { right: 40px; top: 70px; }
  .card--front .brand__name { color: var(--ink-dark); }
  .card--front .brand__tagline { color: var(--ink-grey); }

  .person__tab {
    position: absolute; left: 0; top: 235px;
    width: 17px; height: 44px;
    background: var(--brand-blue);
    border-radius: 0 6px 6px 0;
  }
  .person__name {
    position: absolute; left: 39px; top: 228px;
    font-weight: 600; font-size: 26px;
    color: var(--brand-blue);
    text-transform: uppercase;
  }
  .person__role {
    position: absolute; left: 39px; right: 41px; top: 262px;
    display: flex; align-items: center; gap: 6px;
    font-size: 19px; color: var(--ink-dark);
  }
  .person__role::after {
    content: ""; flex: 1; height: 1px; background: var(--rule);
    margin-top: 4px;
  }
  .contact {
    position: absolute; left: 39px; top: 298px;
    list-style: none;
  }
  .contact__item {
    display: flex; align-items: center; gap: 10px;
    font-size: 18px; color: var(--ink-grey);
    height: 28px;
  }
  .contact__icon { width: 17px; height: 17px; fill: var(--brand-blue); }
  .social { position: absolute; right: 40px; top: 335px; display: flex; gap: 4px; }
  .social__dot { width: 37px; height: 37px; border-radius: 50%; }
  .social__dot--one { background: #3b5998; }
  .social__dot--two { background: #29a9e1; }

  .back__backdrop {
    position: absolute; inset: 0;
    background:
      linear-gradient(150deg, transparent 0 52%, #2a2a2a 60%, #1b1b1b 72%, #0d0d0d 100%),
      var(--card-black);
  }
  .card--back .brand { left: 0; right: 0; top: 172px; }
  .card--back .brand__name { color: var(--ink-light); }
  .card--back .brand__tagline { color: var(--tagline-grey); }
  .services {
    position: absolute; left: 0; right: 0; top: 340px;
    text-align: center;
    font-style: italic; font-size: 19px; color: #ffffff;
  }
  .services__sep {
    display: inline-block; width: 7px; height: 7px;
    background: var(--brand-blue);
    transform: rotate(45deg);
    margin: 0 5px 3px;
  }
</style>
</head>
<body>
  <section class="card card--front">
    <div class="brand">
      <div class="brand__name">Muddle to Marvel</div>
      <div class="brand__tagline">Cleaning Services</div>
    </div>

    <div class="person__tab"></div>
    <div class="person__name">Teodoro Perlas</div>
    <div class="person__role">CEO/Founder</div>

    <ul class="contact">
      <li class="contact__item">
        <svg class="contact__icon" viewBox="0 0 24 24"><path d="M6.6 10.8a15.1 15.1 0 0 0 6.6 6.6l2.2-2.2c.3-.3.7-.4 1-.2 1.1.4 2.3.6 3.6.6.6 0 1 .4 1 1V20c0 .6-.4 1-1 1A17 17 0 0 1 3 4c0-.6.4-1 1-1h3.5c.6 0 1 .4 1 1 0 1.3.2 2.5.6 3.6.1.3 0 .7-.2 1z"/></svg>
        418-635-0247
      </li>
      <li class="contact__item">
        <svg class="contact__icon" viewBox="0 0 24 24"><path d="M2 5h20v14H2z M2 5l10 8 10-8" fill="var(--brand-blue)"/><path d="M3 6l9 7 9-7" fill="none" stroke="#fff" stroke-width="1.8"/></svg>
        hello@muddlemarvel.com
      </li>
      <li class="contact__item">
        <svg class="contact__icon" viewBox="0 0 24 24"><circle cx="12" cy="12" r="10"/><path d="M2 12h20M12 2c3 3 3 17 0 20M12 2c-3 3-3 17 0 20" fill="none" stroke="#fff" stroke-width="1.4"/></svg>
        www.muddlemarvel.com
      </li>
    </ul>

    <div class="social">
      <span class="social__dot social__dot--one"></span>
      <span class="social__dot social__dot--two"></span>
    </div>
  </section>

  <section class="card card--back">
    <div class="back__backdrop" role="img" aria-label="Black background with a soft diagonal sheen and scattered faint blue sparkle stars"></div>
    <div class="brand">
      <div class="brand__name">Muddle to Marvel</div>
      <div class="brand__tagline">Cleaning Services</div>
    </div>
    <p class="services">Industrial<span class="services__sep"></span>Commercial<span class="services__sep"></span>Residential</p>
  </section>
</body>
</html>
```